Business IT Services Billboard to attract local small businesses

We are Brivolane, a premier Managed Service Provider (MSP) specializing in comprehensive IT services and VOIP phone solutions exclusively for businesses. Our goal is to create a dynamic and visually engaging billboard advertisement that not only highlights our cutting-edge IT solutions but also emphasizes our state-of-the-art VOIP phone services. This billboard should communicate our commitment to providing innovative, reliable, and holistic technology solutions.
Target Market(s)
small business
Industry/Entity Type
Information Technology
Colors
Designer to choose colors to be used in the design.
Look and feel
Each slider illustrates characteristics of the customer's brand and the style your logo design should communicate.

```html
<!DOCTYPE html>
<html lang="en">
<head>
<meta charset="utf-8">
<title>Brivolane – Business IT &amp; VOIP Billboard</title>
<link href="https://fonts.googleapis.com/css2?family=Montserrat:wght@600;700;800&family=Poppins:wght@500;600&display=swap" rel="stylesheet">
<style>
  :root {
    --page-bg: #ffffff;
    --board-bg: #eef0f3;
    --ink-black: #111214;
    --brand-blue: #1e90d6;
    --navy: #1b2a5e;
    --white: #ffffff;
    --photo-light: #e4e6ea;
    --photo-mid: #cfd3d9;
  }
  * { margin: 0; padding: 0; box-sizing: border-box; }
  html, body {
    width: 1200px;
    height: 1200px;
    overflow: hidden;
    background: var(--page-bg);
  }
  .canvas {
    position: relative;
    width: 1200px;
    height: 1200px;
    display: flex;
    align-items: center;
    justify-content: center;
  }
  .billboard {
    position: relative;
    width: 1120px;
    height: 480px;
    background: var(--board-bg);
    overflow: hidden;
  }
  .photo {
    position: absolute;
    left: 0;
    top: 190px;
    width: 420px;
    height: 290px;
    background: linear-gradient(120deg, var(--photo-light) 0%, var(--photo-mid) 60%, var(--board-bg) 100%);
  }
  .headline-band {
    position: absolute;
    left: 0;
    top: 0;
    width: 920px;
    height: 190px;
    background: var(--ink-black);
    border-bottom-right-radius: 70px;
    padding: 44px 0 0 50px;
  }
  .headline {
    font-family: "Montserrat", sans-serif;
    font-weight: 800;
    font-size: 40px;
    line-height: 1.22;
    letter-spacing: 1px;
    color: var(--white);
    text-transform: uppercase;
    white-space: nowrap;
  }
  .tagline {
    position: absolute;
    left: 400px;
    top: 232px;
    width: 460px;
    font-family: "Poppins", sans-serif;
    font-weight: 600;
    font-size: 22px;
    line-height: 1.4;
    color: var(--navy);
    text-align: right;
    white-space: nowrap;
  }
  .brand-name {
    position: absolute;
    right: 20px;
    top: 236px;
    width: 230px;
    font-family: "Montserrat", sans-serif;
    font-weight: 800;
    font-size: 36px;
    color: var(--brand-blue);
    text-align: center;
    white-space: nowrap;
  }
  .cta-tab {
    position: absolute;
    right: 0;
    bottom: 82px;
    width: 300px;
    height: 48px;
    background: var(--ink-black);
    border-top-left-radius: 24px;
    display: flex;
    align-items: center;
    justify-content: flex-end;
    padding-right: 22px;
    font-family: "Poppins", sans-serif;
    font-weight: 600;
    font-size: 22px;
    color: var(--white);
    white-space: nowrap;
  }
  .url-band {
    position: absolute;
    right: 0;
    bottom: 0;
    width: 680px;
    height: 82px;
    background: var(--brand-blue);
    border-top-left-radius: 50px;
    display: flex;
    align-items: center;
    justify-content: flex-end;
    padding-right: 22px;
  }
  .url {
    font-family: "Montserrat", sans-serif;
    font-weight: 700;
    font-size: 44px;
    letter-spacing: 3px;
    color: var(--white);
    white-space: nowrap;
  }
</style>
</head>
<body>
  <main class="canvas">
    <section class="billboard">
      <div class="photo" role="img" aria-label="Photo of a smiling support agent wearing a headset with microphone"></div>
      <div class="headline-band">
        <h1 class="headline">Elevate your business with<br>next-gen IT &amp; VOIP services</h1>
      </div>
      <p class="tagline">Innovative IT and VOIP Solutions<br>Tailored for Your Business Success.</p>
      <div class="brand-name">Brivolane</div>
      <div class="cta-tab">Your Tech Today at</div>
      <div class="url-band">
        <span class="url">www.brivolane.com</span>
      </div>
    </section>
  </main>
</body>
</html>
```